High End Art Gallery Business Card

We're looking for a business card design that is elegant and artful. Foil embossing, blind embossed pattern, or some kind of "extra" element to make it stand out. Standard American size. The back should remain blank or nearly blank so that notes can be written on the back.
Please check our website at kestrelvane.com to see information about our gallery and the type of artwork that we sell.
Included with the files is a brand identity guideline. In addition to the colors listed, we like to incorporate an indigo blue. The business card design in the guideline seems too simplistic. I have included some photos of other business card designs that have caught my eye.
thank you!

Contact Information for Business Card

Marisol Tevard
Gallery Owner
remaining details are in the attached docs

• some kind of natural/organic element to reflect the hand-made nature of all of the original artwork.

```html
<!DOCTYPE html>
<html lang="en">
<head>
<meta charset="utf-8">
<title>Marisol Tevard — Business Card</title>
<link href="https://fonts.googleapis.com/css2?family=Work+Sans:wght@400;500&display=swap" rel="stylesheet">
<style>
  :root {
    --backdrop: #d8c3b1;
    --card-stock: #f6f4ef;
    --foil-gold: #b98a2c;
    --foil-gold-soft: #e9d9b4;
    --emboss-light: #fbfaf6;
    --emboss-shade: rgba(120, 96, 60, 0.22);
    --ink-grey: #6b6966;
  }
  html, body {
    margin: 0;
    padding: 0;
    width: 1200px;
    height: 900px;
    overflow: hidden;
    background: var(--backdrop);
  }
  .canvas {
    position: relative;
    width: 1200px;
    height: 900px;
  }
  .business-card {
    position: absolute;
    left: 371px;
    top: 50px;
    width: 457px;
    height: 800px;
    background: var(--card-stock);
    box-shadow: 0 2px 10px rgba(80, 60, 40, 0.18);
    font-family: "Work Sans", sans-serif;
  }
  .emblem-pattern {
    position: absolute;
    left: 11px;
    top: 8px;
    width: 435px;
    height: 338px;
    border-radius: 6px;
    background:
      radial-gradient(ellipse at 30% 25%, rgba(255, 255, 255, 0.55), transparent 60%),
      radial-gradient(ellipse at 75% 80%, rgba(185, 138, 44, 0.18), transparent 65%),
      linear-gradient(160deg, var(--foil-gold-soft), var(--emboss-light) 55%, var(--foil-gold-soft));
    box-shadow:
      inset 2px 2px 4px var(--emboss-shade),
      inset -2px -2px 4px rgba(255, 255, 255, 0.9);
  }
  .card-details {
    position: absolute;
    left: 52px;
    top: 383px;
    right: 24px;
  }
  .owner-name {
    margin: 0;
    font-size: 27px;
    font-weight: 500;
    letter-spacing: 0.16em;
    color: var(--foil-gold);
    text-transform: uppercase;
    line-height: 1;
  }
  .owner-role {
    margin: 10px 0 0;
    font-size: 19px;
    font-weight: 500;
    letter-spacing: 0.06em;
    color: var(--ink-grey);
  }
  .gold-rule {
    width: 52px;
    height: 2px;
    background: var(--foil-gold);
    margin: 43px 0 34px;
  }
  .contact-list, .address {
    margin: 0;
    font-size: 19px;
    font-weight: 500;
    letter-spacing: 0.08em;
    color: var(--ink-grey);
    line-height: 29px;
    font-style: normal;
  }
  .contact-list .label {
    display: inline-block;
    width: 46px;
  }
  .address {
    margin-top: 29px;
  }
</style>
</head>
<body>
<div class="canvas">
  <section class="business-card">
    <div class="emblem-pattern" role="img" aria-label="Embossed gold foil grid of the gallery emblem, seven across and five rows down"></div>
    <div class="card-details">
      <h1 class="owner-name">Marisol Tevard</h1>
      <p class="owner-role">Gallery Owner</p>
      <div class="gold-rule"></div>
      <p class="contact-list">
        <span class="label">P:</span>(808) 555-0147<br>
        <span class="label">E:</span>info@kestrelvane.com<br>
        <span class="label">W:</span>www.kestrelvane.com
      </p>
      <address class="address">
        214 Halekula Lane<br>
        Honolulu, HI 96813 USA
      </address>
    </div>
  </section>
</div>
</body>
</html>
```